Newsletter Design for Travel - Group -Event Agency

We are looking for a standard Newsletter Design which we can use regularly to send out to a number of clients. The idea is to add 1 or more pictures and a promotion or program as well as some possible news. We are a travel agency and want to promote our products in either the travel sector (B2C) or event and group sector (B2B , see our company logo enclosed.

Target Market(s)

We have different target markets, but in the end it's always connected to the travel industry

Industry/Entity Type

Events

Font styles to use
Sans Serif

Colors
3176b5
eaf1f7

Requirements
Must have
• Area to upload picture(s), text field and business data (website, linkedin, facebook, instagram, tel and e-mail contacts. Subscribe/unsubscrive
Nice to have
• optional CTA Buttom, p.e. "make a virutal appointment" or similar
Should not have
• should stay with the colours of our logo / website - grey, a bit blue

```html
<!DOCTYPE html>
<html lang="en">
<head>
<meta charset="utf-8">
<title>Luso Horizon Newsletter</title>
<link href="https://fonts.googleapis.com/css2?family=Montserrat:wght@800;900&family=Roboto:wght@400;500&family=Lato:wght@400&display=swap" rel="stylesheet">
<style>
  :root {
    --brand-blue: #0575bd;
    --ink: #000000;
    --body-grey: #666666;
    --footer-bg: #000000;
    --paper: #ffffff;
    --photo-green: #6f7f5a;
    --photo-warm: #b89a78;
    --photo-light: #d9dde2;
  }
  * { margin: 0; padding: 0; box-sizing: border-box; }
  html, body { width: 1200px; height: 3588px; overflow: hidden; background: var(--paper); }
  body { position: relative; font-family: "Roboto", sans-serif; }
  .abs { position: absolute; }

  .brand { left: 0; width: 1200px; top: 30px; text-align: center; }
  .brand-name { font-family: "Roboto", sans-serif; font-weight: 500; font-size: 50px; letter-spacing: 4px; color: var(--ink); line-height: 1; }
  .brand-tag { font-family: "Roboto", sans-serif; font-weight: 500; font-size: 15px; letter-spacing: 6px; color: var(--brand-blue); margin-top: 18px; }

  .photo { display: block; }
  .hero-photo { left: 150px; top: 160px; width: 489px; height: 650px; background: linear-gradient(160deg, var(--photo-green), #4d5b3e 55%, var(--photo-warm)); }
  .hero-panel { left: 538px; top: 273px; width: 512px; height: 660px; background: var(--brand-blue); padding: 87px 0 0 49px; }
  .hero-title { font-family: "Montserrat", sans-serif; font-weight: 900; font-size: 58px; line-height: 67px; color: var(--paper); }
  .hero-sub { font-size: 30px; letter-spacing: 3.5px; color: var(--paper); margin-top: 22px; }
  .btn { display: inline-flex; align-items: center; justify-content: center; background: var(--ink); color: var(--paper); font-size: 27px; text-decoration: none; }
  .hero-btn { margin-top: 52px; width: 388px; height: 75px; }

  .section-title { font-family: "Montserrat", sans-serif; font-weight: 900; font-size: 58px; color: var(--ink); line-height: 1; }
  .about-title { left: 0; width: 1200px; top: 1020px; text-align: center; }
  .about-text { left: 180px; width: 840px; top: 1097px; text-align: center; font-size: 27px; line-height: 40.5px; color: var(--body-grey); }

  .promo-photo { left: 0; top: 1326px; width: 1200px; height: 454px; background: linear-gradient(100deg, #5a4a3e, #3a3632 40%, #8c7f70 70%, #d6c8ad); }
  .second-photo { left: 150px; top: 1884px; width: 900px; height: 627px; background: linear-gradient(135deg, var(--photo-light), #c9d4dd 45%, #9aa9bb 75%, #7e6f62); }
  .promo-panel { left: 150px; top: 1550px; width: 496px; height: 466px; background: var(--brand-blue); padding: 42px 0 0 60px; }
  .promo-title { color: var(--paper); }
  .promo-text { font-size: 27px; line-height: 42px; color: var(--paper); margin-top: 26px; width: 390px; }
  .promo-btn { margin-top: 32px; width: 268px; height: 75px; }

  .events-title { left: 150px; top: 2568px; }
  .events-text { left: 150px; width: 900px; top: 2648px; font-size: 27px; line-height: 42px; color: var(--body-grey); text-align: justify; }
  .events-btn { left: 150px; top: 2854px; width: 268px; height: 75px; position: absolute; }

  .footer { left: 0; top: 3034px; width: 1200px; height: 306px; background: var(--footer-bg); color: var(--paper); }
  .footer-title { position: absolute; left: 150px; top: 75px; font-size: 30px; font-weight: 500; }
  .contact-line { position: absolute; display: flex; align-items: center; gap: 20px; font-size: 27px; }
  .contact-line svg { flex: none; }
  .socials { position: absolute; left: 795px; top: 211px; display: flex; gap: 27px; }
  .socials span { width: 20px; height: 20px; border-radius: 50%; background: var(--paper); display: block; }

  .sub-btn { top: 3427px; height: 60px; display: flex; align-items: center; justify-content: center; font-size: 21px; font-weight: 500; }
  .subscribe { left: 397px; width: 197px; background: var(--brand-blue); color: var(--paper); }
  .unsubscribe { left: 606px; width: 196px; background: var(--paper); color: var(--ink); box-shadow: 0 1px 8px rgba(0,0,0,0.15); font-weight: 400; }
  .copyright { left: 0; width: 1200px; top: 3535px; text-align: center; font-family: "Lato", sans-serif; font-size: 20px; color: #555; }
  .copyright .company { color: var(--brand-blue); }
</style>
</head>
<body>
  <header class="brand abs">
    <div class="brand-name">LUSO HORIZON</div>
    <div class="brand-tag">TRAVEL - GROUPS - EVENTS</div>
  </header>

  <div class="hero-photo photo abs" role="img" aria-label="Photo from above of a traveller in a green hat typing on a laptop on a green rug"></div>
  <section class="hero-panel abs">
    <h1 class="hero-title">WELCOME<br>TO<br>LUSO<br>HORIZON</h1>
    <p class="hero-sub">TRAVEL-GROUPS-EVENTS</p>
    <a class="btn hero-btn" href="#">Make A Virutal Appointment</a>
  </section>

  <h2 class="section-title about-title abs">ABOUT US</h2>
  <p class="about-text abs">Lorem ipsum dolor sit amet, consectetur adipiscing elit, sed do eiusmod tempor incididunt ut labore et dolore magna aliqua. Ut enim ad minim veniam, quis nostrud exercitation ullamco laboris nisi ut aliquip ex ea commodo consequat.</p>

  <div class="promo-photo photo abs" role="img" aria-label="Photo of travellers meeting an agent in front of a world map wall, with a sun hat and suitcase"></div>
  <div class="second-photo photo abs" role="img" aria-label="Photo of a couple browsing a travel brochure with an agent at a desk"></div>
  <section class="promo-panel abs">
    <h2 class="section-title promo-title">PROMOTION</h2>
    <p class="promo-text">Lorem ipsum dolor sit amet, consectetur adipiscing elit, sed do eiusmod tempor incididunt ut labore et dolore magna</p>
    <a class="btn promo-btn" href="#">Read More</a>
  </section>

  <h2 class="section-title events-title abs">EVENTS</h2>
  <p class="events-text abs">Lorem ipsum dolor sit amet, consectetur adipiscing elit, sed do eiusmod tempor incididunt ut labore et dolore magna aliqua. Ut enim ad minim veniam, quis nostrud exercitation ullamco laboris nisi ut aliquip ex ea commodo consequat.</p>
  <a class="btn events-btn" href="#">Read More</a>

  <footer class="footer abs">
    <div class="footer-title">Contact Us</div>
    <div class="contact-line" style="left:150px; top:150px;">
    <svg width="26" height="26" viewBox="0 0 24 24"><path fill="#fff" d="M6.6 10.8c1.4 2.8 3.8 5.1 6.6 6.6l2.2-2.2c.3-.3.7-.4 1-.2 1.1.4 2.3.6 3.6.6.6 0 1 .4 1 1V20c0 .6-.4 1-1 1C10.6 21 3 13.4 3 4c0-.6.4-1 1-1h3.5c.6 0 1 .4 1 1 0 1.3.2 2.5.6 3.6.1.3 0 .7-.2 1L6.6 10.8z"/></svg>
      <span>+8 555 010 2040</span>
    </div>
    <div class="contact-line" style="left:150px; top:194px;">
      <svg width="30" height="24" viewBox="0 0 30 24"><rect x="0" y="2" width="30" height="20" rx="2" fill="#fff"/><path d="M1 4l14 10L29 4" stroke="#000" stroke-width="2.5" fill="none"/></svg>
      <span>hello@lusohorizon.example</span>
    </div>
    <div class="contact-line" style="left:795px; top:150px;">
      <svg width="26" height="26" viewBox="0 0 26 26"><circle cx="13" cy="13" r="12" fill="#fff"/><path d="M6 9c3 0 4 2 3 4s1 4 3 4M15 4c-1 3 2 4 4 4s3 2 2 5" stroke="#000" stroke-width="2.5" fill="none"/></svg>
      <span>www.lusohorizon.example</span>
    </div>
    <div class="socials" aria-label="Social channels"><span></span><span></span><span></span></div>
  </footer>

  <a class="sub-btn subscribe abs" href="#">Subscribe</a>
  <a class="sub-btn unsubscribe abs" href="#">Unsubscribe</a>
  <p class="copyright abs">Copyrights © <span class="company">The Company name 2021</span> | Allrights Reserved</p>
</body>
</html>
```